Logo needed for business card

Velquist Pty Ltd is in the business of healthcare and ecommerce.

We own and manage pharmacies and online health ecomerce sites.

We provide ecommerce consultants for companies looking for an ecommerce business startegy.

Think of it as the umbrella under which several healthcare brands may sit.

When I think of Velquist, I visulaise slick black/metalic colours, so please stay away from the common blue and green colours that seem to be so popular in this field.

Target Market(s)

CEOs and COOs

Industry/Entity Type

Healthcare

Contact Information for Business Card

Tessa Lindqvist
Director
Velquist Pty Ltd
4/362 Fennick Pde
Brellton, NSW 2148

Requirements
Must have
• Design must have scope to be implemented on the company's website and letterheads etc.

```html
<!DOCTYPE html>
<html lang="en">
<head>
<meta charset="utf-8">
<title>Velquist Business Card</title>
<link rel="stylesheet" href="https://fonts.googleapis.com/css2?family=Open+Sans:wght@400;600;700&display=swap">
<style>
  :root {
    --page-bg: #e6e7e9;
    --card-dark: #494d56;
    --card-light-top: #ffffff;
    --card-light-bottom: #ececec;
    --ink-dark: #3d414b;
    --ink-soft: #4a4e57;
    --mark-light: #d9dadc;
    --accent-red: #d3322b;
    --watermark: #e3e4e5;
  }
  * { margin: 0; padding: 0; box-sizing: border-box; }
  html, body {
    width: 1200px; height: 900px; overflow: hidden;
    background: var(--page-bg);
    font-family: "Open Sans", Arial, sans-serif;
  }
  .stage { position: relative; width: 1200px; height: 900px; }
  .card {
    position: absolute; left: 280px; width: 640px; height: 365px;
    overflow: hidden; border-radius: 3px;
    box-shadow: 0 10px 28px rgba(0,0,0,0.22);
  }
  /* Back */
  .card--back { top: 55px; background: var(--card-dark); }
  .back-brand {
    position: absolute; left: 250px; top: 128px;
    display: flex; align-items: center; gap: 18px;
  }
  .back-brand .wordmark {
    font-size: 52px; font-weight: 700; color: var(--mark-light); letter-spacing: 0.5px;
  }
  .back-brand .dot {
    width: 56px; height: 56px; border-radius: 50%;
    border: 7px solid var(--mark-light);
  }
  .back-rule {
    position: absolute; left: 0; top: 214px; width: 512px; height: 1.5px;
    background: var(--accent-red);
  }
  /* Front */
  .card--front {
    top: 480px;
    background: linear-gradient(160deg, var(--card-light-top), var(--card-light-bottom));
  }
  .watermark-circle {
    position: absolute; left: 335px; top: 40px; width: 400px; height: 400px;
    border-radius: 50%; border: 34px solid var(--watermark);
  }
  .front-brand {
    position: absolute; left: 42px; top: 44px;
    display: flex; align-items: center; gap: 16px;
  }
  .front-brand .wordmark {
    font-size: 34px; font-weight: 700; color: var(--ink-dark);
  }
  .front-brand .dot {
    width: 40px; height: 40px; border-radius: 50%;
    border: 5px solid var(--ink-dark);
  }
  .person {
    position: absolute; right: 356px; top: 176px; text-align: right;
  }
  .person .name { font-size: 29px; font-weight: 400; color: var(--ink-soft); line-height: 1.1; }
  .person .role { font-size: 20px; font-weight: 600; color: var(--accent-red); letter-spacing: 0.5px; margin-top: 2px; }
  .divider {
    position: absolute; left: 306px; top: 200px; width: 1.5px; height: 170px;
    background: var(--accent-red);
  }
  .contact {
    position: absolute; left: 322px; top: 206px;
    font-size: 16px; color: var(--ink-dark); line-height: 1.35;
  }
  .contact .label { color: var(--accent-red); font-weight: 700; display: inline-block; width: 18px; }
  .company {
    position: absolute; left: 330px; top: 280px;
    font-size: 16px; color: var(--ink-dark); line-height: 1.3;
  }
  .company .company-name { font-weight: 700; }
</style>
</head>
<body>
<main class="stage">
  <section class="card card--back" aria-label="Business card back">
    <div class="back-brand">
      <span class="wordmark">Velquist</span>
      <span class="dot" aria-hidden="true"></span>
    </div>
    <div class="back-rule"></div>
  </section>

  <section class="card card--front" aria-label="Business card front">
    <div class="watermark-circle" aria-hidden="true"></div>
    <div class="front-brand">
      <span class="wordmark">Velquist</span>
      <span class="dot" aria-hidden="true"></span>
    </div>
    <div class="person">
      <p class="name">Tessa Lindqvist</p>
      <p class="role">DIRECTOR</p>
    </div>
    <div class="divider"></div>
    <div class="contact">
      <p><span class="label">t</span>(222) 418 620 377</p>
      <p><span class="label">e</span>name@velquist.com</p>
    </div>
    <address class="company" style="font-style: normal;">
      <p class="company-name">Velquist Pty Ltd</p>
      <p>4/362 Fennick Pde</p>
      <p>Brellton, NSW 2148</p>
    </address>
  </section>
</main>
</body>
</html>
```